Bluewren Business Cards

Name Tomas Velikor
Title Mortgage Originator
Phone (800) 641-2705 x32
Direct (571) 362-8104
Email tvelikor@bluewrenhomeloans.example
NMLS #3804427
Name Lien Vo
Title Mortgage Originator
Location (800) 641-2705 x55
Direct (440) 296-5081
Email lvo@bluewrenhomeloans.example
NMLS #3719046
Name Solomon Ked-Ravi
Title Mortgage Originator
Location (800) 641-2705 x56
Direct (202) 374-6019
Email skedravi@bluewrenhomeloans.example
NMLS #3748510
Name Roselle Dunfield
Title Mortgage Originator
Location (800) 641-2705 x57
Direct (240) 538-2274
Email rdunfield@bluewrenhomeloans.example
NMLS #3692384
Name Dana Whitcombe
Title Mortgage Originator
Location (800) 641-2705 x58
Direct (540) 681-3926
Email dwhitcombe@bluewrenhomeloans.example
NMLS #3657019
Name Idris Holt
Title Mortgage Originator
Location (800) 641-2705 x59
Direct (240) 163-8852
Email iholt@bluewrenhomeloans.example
NMLS #3781462
Name Zora Lund
Title Mortgage Originator
Location (800) 641-2705 x60
Direct (202) 449-2637
Email zora@zorafindshomes.example
NMLS #3795038
Contact Information for Business Card
Name Tomas Velikor Title Mortgage Originator Phone (800) 641-2705 x32 Direct (571) 362-8104 Email tvelikor@bluewrenhomeloans.example NMLS #3804427 Name Lien Vo Title Mortgage Originator Location (800) 641-2705 x55 Direct (440) 296-5081 Email lvo@bluewrenhomeloans.example NMLS #3719046 Name Solomon Ked-Ravi Title Mortgage Originator Location (800) 641-2705 x56 Direct (202) 374-6019 Email skedravi@bluewrenhomeloans.example NMLS #3748510 Name Roselle Dunfield Title Mortgage Originator Location (800) 641-2705 x57 Direct (240) 538-2274 Email rdunfield@bluewrenhomeloans.example NMLS #3692384 Name Dana Whitcombe Title Mortgage Originator Location (800) 641-2705 x58 Direct (540) 681-3926 Email dwhitcombe@bluewrenhomeloans.example NMLS #3657019 Name Idris Holt Title Mortgage Originator Location (800) 641-2705 x59 Direct (240) 163-8852 Email iholt@bluewrenhomeloans.example NMLS #3781462 Name Zora Lund Title Mortgage Originator Location (800) 641-2705 x60 Direct (202) 449-2637 Email zora@zorafindshomes.example NMLS #3795038

```html
<!DOCTYPE html>
<html lang="en">
<head>
<meta charset="utf-8">
<title>Bluewren Business Cards</title>
<link rel="stylesheet" href="https://fonts.googleapis.com/css2?family=Montserrat:wght@400;700&display=swap">
<style>
:root{
  --board:#cdcdcd;
  --card:#ffffff;
  --ink:#1a1a1a;
  --text:#2b2b2b;
  --rule:#0d0d0d;
  --green:#4b6b3f;
  --teal:#1e4a63;
  --plum:#6a4a58;
  --plum-name:#5a3343;
  --maroon:#5c2530;
  --navy:#13235a;
}
*{box-sizing:border-box;margin:0;padding:0}
html,body{width:1104px;height:1200px;overflow:hidden}
body{background:var(--board);position:relative;font-family:"Montserrat",Arial,sans-serif;color:var(--text)}
.card{position:absolute;width:328px;height:188px;background:var(--card);border-radius:14px;overflow:hidden;
  box-shadow:0 6px 14px rgba(0,0,0,.28);--accent:var(--navy);--name:var(--ink)}
.photo{position:absolute;z-index:1}
.details{position:absolute;top:47px;z-index:2;white-space:nowrap}
.photo-left .details{left:160px}
.photo-right .details{left:20px}
.name{font-weight:700;font-size:14.5px;color:var(--name);letter-spacing:.1px;line-height:1}
.title{font-size:9.2px;margin-top:6px;line-height:1}
.contacts{list-style:none;margin-top:10px}
.contacts li{display:flex;align-items:center;gap:5px;font-size:8.6px;line-height:1;height:14px}
.contacts li.email{font-size:7.2px;letter-spacing:-.2px;height:17px}
.contacts svg{width:9px;height:9px;flex:none;fill:var(--icon,var(--accent))}
.footer{position:absolute;left:0;bottom:0;width:328px;height:16px;z-index:3}
.nmls{position:absolute;bottom:1px;z-index:4;color:#fff;font-size:9px;letter-spacing:.2px;line-height:13px}
.photo-left .nmls{left:225px}
.photo-right .nmls{left:21px}
.theme-green{--accent:var(--green);--icon:#6a9a5a}
.theme-teal{--accent:var(--teal);--name:var(--teal)}
.theme-plum{--accent:var(--plum);--name:var(--plum-name)}
.theme-maroon{--accent:var(--plum);--name:var(--maroon)}
.theme-navy{--accent:var(--navy);--name:var(--navy)}
.theme-dark{--accent:var(--plum);--icon:var(--ink)}
</style>
</head>
<body>
<svg width="0" height="0" style="position:absolute" aria-hidden="true">
  <symbol id="icon-phone" viewBox="0 0 24 24"><path d="M6.6 2.5c.6-.4 1.4-.3 1.8.3l2.3 3.4c.4.6.3 1.3-.2 1.8l-1.4 1.3c1 2.2 2.8 4 5 5l1.3-1.4c.5-.5 1.2-.6 1.8-.2l3.4 2.3c.6.4.7 1.2.3 1.8l-1.5 2.2c-.6.9-1.7 1.3-2.7 1C9.8 18.4 5.6 14.2 3.8 7.3c-.3-1 .1-2.1 1-2.7z"/><path d="M14 3a7 7 0 0 1 7 7h-2a5 5 0 0 0-5-5zm0 3a4 4 0 0 1 4 4h-2a2 2 0 0 0-2-2z"/></symbol>
  <symbol id="icon-mail" viewBox="0 0 24 24"><path d="M2 5h20v14H2z M4 7v.5l8 5.5 8-5.5V7z" fill-rule="evenodd"/></symbol>
</svg>

<!-- Tomas Velikor -->
<article class="card photo-left theme-green" style="left:190px;top:102px">
  <div class="photo" role="img" aria-label="Portrait of Tomas Velikor in a green shirt and dark tie" style="left:5px;top:6px;width:138px;height:172px;background:linear-gradient(180deg,#ffffff 0%,#ffffff 22%,#7fb56a 48%,#5f9a4f 100%);border-radius:60px 60px 0 0"></div>
  <div class="details">
    <h2 class="name">Tomas Velikor</h2>
    <p class="title">Mortgage Originator</p>
    <ul class="contacts">
      <li><svg><use href="#icon-phone"/></svg>(800) 641-2705 x32</li>
      <li><svg><use href="#icon-phone"/></svg>Direct (571) 362-8104</li>
      <li class="email"><svg><use href="#icon-mail"/></svg>tvelikor@bluewrenhomeloans.example</li>
    </ul>
  </div>
  <svg class="footer" viewBox="0 0 328 16" aria-hidden="true"><rect x="0" y="2.5" width="186" height="3" fill="var(--rule)"/><polygon points="185,2 328,2 328,16 172,16" fill="var(--green)"/></svg>
  <p class="nmls">NMLS #3804427</p>
</article>

<!-- Lien Vo -->
<article class="card photo-right theme-teal" style="left:551px;top:93px">
  <div class="photo" role="img" aria-label="Portrait of Lien Vo in a navy suit and glasses" style="left:182px;top:12px;width:146px;height:166px;background:linear-gradient(180deg,#ffffff 0%,#ffffff 30%,#2d4d74 62%,#1c3554 100%);border-radius:70px 70px 0 0"></div>
  <div class="details" style="top:53px">
    <h2 class="name">Lien Vo</h2>
    <p class="title">Mortgage Originator</p>
    <ul class="contacts">
      <li><svg><use href="#icon-phone"/></svg>Location (800) 641-2705 x55</li>
      <li><svg><use href="#icon-phone"/></svg>Direct (440) 296-5081</li>
      <li class="email"><svg><use href="#icon-mail"/></svg>lvo@bluewrenhomeloans.example</li>
    </ul>
  </div>
  <svg class="footer" viewBox="0 0 328 16" aria-hidden="true"><polygon points="0,2 130,2 142,16 0,16" fill="var(--teal)"/><rect x="138" y="4.5" width="190" height="3" fill="var(--rule)"/></svg>
  <p class="nmls">NMLS #3719046</p>
</article>

<!-- Solomon Ked-Ravi -->
<article class="card photo-right theme-plum" style="left:189px;top:330px">
  <div class="photo" role="img" aria-label="Portrait of Solomon Ked-Ravi in a burgundy blazer and black turtleneck" style="left:186px;top:10px;width:142px;height:168px;background:linear-gradient(180deg,#ffffff 0%,#ffffff 25%,#6e4048 60%,#3a2a2e 100%);border-radius:60px 60px 0 0"></div>
  <div class="details" style="top:55px">
    <h2 class="name">Solomon Ked-Ravi</h2>
    <p class="title">Mortgage Originator</p>
    <ul class="contacts">
      <li><svg><use href="#icon-phone"/></svg>(800) 641-2705 x56</li>
      <li><svg><use href="#icon-phone"/></svg>Direct (202) 374-6019</li>
      <li class="email"><svg><use href="#icon-mail"/></svg>skedravi@bluewrenhomeloans.example</li>
    </ul>
  </div>
  <svg class="footer" viewBox="0 0 328 16" aria-hidden="true"><polygon points="0,2 130,2 142,16 0,16" fill="var(--plum)"/><rect x="138" y="4.5" width="190" height="3" fill="var(--rule)"/></svg>
  <p class="nmls">NMLS #3748510</p>
</article>

<!-- Roselle Dunfield -->
<article class="card photo-right theme-maroon" style="left:551px;top:326px">
  <div class="photo" role="img" aria-label="Portrait of Roselle Dunfield in a pink suit with a floral waist wrap" style="left:222px;top:14px;width:100px;height:164px;background:linear-gradient(180deg,#ffffff 0%,#ffffff 18%,#e3a5ad 45%,#5a6a92 60%,#e0a3ab 75%,#eab3ba 100%);border-radius:40px 40px 0 0"></div>
  <div class="details" style="top:54px">
    <h2 class="name">Roselle Dunfield</h2>
    <p class="title">Mortgage Originator</p>
    <ul class="contacts">
      <li><svg><use href="#icon-phone"/></svg>(800) 641-2705 x57</li>
      <li><svg><use href="#icon-phone"/></svg>Direct (240) 538-2274</li>
      <li class="email"><svg><use href="#icon-mail"/></svg>rdunfield@bluewrenhomeloans.example</li>
    </ul>
  </div>
  <svg class="footer" viewBox="0 0 328 16" aria-hidden="true"><polygon points="0,2 130,2 142,16 0,16" fill="var(--plum)"/><rect x="138" y="4.5" width="190" height="3" fill="var(--rule)"/></svg>
  <p class="nmls">NMLS #3692384</p>
</article>

<!-- Dana Whitcombe -->
<article class="card photo-left theme-dark" style="left:189px;top:573px">
  <div class="photo" role="img" aria-label="Portrait of Dana Whitcombe in a black blazer, on the phone" style="left:14px;top:0;width:136px;height:178px;background:linear-gradient(180deg,#2a2020 0%,#6b4a3a 30%,#2b2b2e 60%,#1f1f22 100%);border-radius:60px 70px 0 0"></div>
  <div class="details">
    <h2 class="name">Dana Whitcombe</h2>
    <p class="title">Mortgage Originator</p>
    <ul class="contacts">
      <li><svg><use href="#icon-phone"/></svg>(800) 641-2705 x58</li>
      <li><svg><use href="#icon-phone"/></svg>Direct (540) 681-3926</li>
      <li class="email"><svg><use href="#icon-mail"/></svg>dwhitcombe@bluewrenhomeloans.example</li>
    </ul>
  </div>
  <svg class="footer" viewBox="0 0 328 16" aria-hidden="true"><rect x="0" y="2.5" width="186" height="3" fill="var(--rule)"/><polygon points="185,2 328,2 328,16 172,16" fill="var(--plum)"/></svg>
  <p class="nmls">NMLS #3657019</p>
</article>

<!-- Idris Holt -->
<article class="card photo-left theme-navy" style="left:560px;top:587px">
  <div class="photo" role="img" aria-label="Portrait of Idris Holt in a navy pinstripe blazer" style="left:0;top:17px;width:148px;height:161px;background:linear-gradient(180deg,#ffffff 0%,#b07a5a 20%,#8a5a40 55%,#1f3a7a 75%,#1a2f66 100%);border-radius:0 80px 0 0"></div>
  <div class="details">
    <h2 class="name">Idris Holt</h2>
    <p class="title">Mortgage Originator</p>
    <ul class="contacts">
      <li><svg><use href="#icon-phone"/></svg>(800) 641-2705 x59</li>
      <li><svg><use href="#icon-phone"/></svg>Direct (240) 163-8852</li>
      <li class="email"><svg><use href="#icon-mail"/></svg>iholt@bluewrenhomeloans.example</li>
    </ul>
  </div>
  <svg class="footer" viewBox="0 0 328 16" aria-hidden="true"><rect x="0" y="2.5" width="186" height="3" fill="var(--rule)"/><polygon points="185,2 328,2 328,16 172,16" fill="var(--navy)"/></svg>
  <p class="nmls">NMLS #3781462</p>
</article>

<!-- Zora Lund -->
<article class="card photo-left theme-navy" style="left:326px;top:848px">
  <div class="photo" role="img" aria-label="Portrait of Zora Lund in a white blazer" style="left:12px;top:16px;width:136px;height:162px;background:linear-gradient(180deg,#ffffff 0%,#d9d6d2 18%,#7a5040 35%,#f2f0ee 60%,#e6e4e2 100%);border-radius:60px 60px 0 0"></div>
  <div class="details">
    <h2 class="name">Zora Lund</h2>
    <p class="title">Mortgage Originator</p>
    <ul class="contacts">
      <li><svg><use href="#icon-phone"/></svg>(800) 641-2705 x60</li>
      <li><svg><use href="#icon-phone"/></svg>Direct (202) 449-2637</li>
      <li class="email"><svg><use href="#icon-mail"/></svg>zora@zorafindshomes.example</li>
    </ul>
  </div>
  <svg class="footer" viewBox="0 0 328 16" aria-hidden="true"><rect x="0" y="2.5" width="186" height="3" fill="var(--rule)"/><polygon points="185,2 328,2 328,16 172,16" fill="var(--navy)"/></svg>
  <p class="nmls">NMLS #3795038</p>
</article>
</body>
</html>
```